Redesign of Business Card to look more professional and stand out

Business card design. You can lean more about our company by going to dkrfabworks.example. Raised letters would be nice. Company name & Address
DK&R
418 Wendlow Ridge Drive, Suite 340
Birmingham, AL 35242

You can use my name and title: Glenn Harwick
Business Development Manager

Target Market(s)

Heavy Industrial market, i.e. utilities, chemical plants, paper mills, construction companies

Industry/Entity Type

Construction

Contact Information for Business Card

We provide Project Management & Project Support Services

Font styles to use
Serif

Requirements
Must have
• Company name & Address
• DK&R
• 418 Wendlow Ridge Drive, Suite 340
• Birmingham, AL 35242
Nice to have
• ideas for the back of the card
Should not have
• no crazy colors. needs to look professional and standout.

```html
<!DOCTYPE html>
<html lang="en">
<head>
<meta charset="utf-8">
<title>DK&amp;R Business Card</title>
<link href="https://fonts.googleapis.com/css2?family=Open+Sans:wght@400;600;800&display=swap" rel="stylesheet">
<style>
  :root {
    --navy: #1d3566;
    --royal-top: #4b68b2;
    --royal-bottom: #354f8e;
    --rust: #c4541f;
    --paper: #f4f4f4;
    --ink-grey: #6d7480;
    --backdrop: #2b2b2b;
    --white: #ffffff;
  }
  * { margin: 0; padding: 0; box-sizing: border-box; }
  html, body { width: 1200px; height: 900px; overflow: hidden; }
  body {
    background: var(--backdrop);
    font-family: "Open Sans", Arial, sans-serif;
    position: relative;
  }
  .card {
    position: absolute;
    left: 250px;
    width: 700px;
    height: 400px;
    border-radius: 18px;
    overflow: hidden;
    box-shadow: 0 12px 30px rgba(0,0,0,.45);
  }

  /* Back of card */
  .card-back {
    top: 30px;
    background: linear-gradient(160deg, var(--royal-top), var(--royal-bottom));
    display: flex;
    flex-direction: column;
    align-items: center;
    justify-content: center;
  }
  .card-back .wordmark {
    color: var(--white);
    font-weight: 800;
    font-size: 150px;
    line-height: 1;
    letter-spacing: 2px;
  }
  .web-rule {
    display: flex;
    align-items: center;
    gap: 12px;
    margin-top: 14px;
    color: var(--white);
    font-size: 15px;
  }
  .web-rule .rule {
    width: 150px;
    height: 1px;
    background: linear-gradient(90deg, rgba(255,255,255,0), rgba(255,255,255,.85));
  }
  .web-rule .rule.right {
    background: linear-gradient(90deg, rgba(255,255,255,.85), rgba(255,255,255,0));
  }

  /* Front of card */
  .card-front {
    top: 470px;
    background: var(--paper);
  }
  .band-top {
    position: absolute; top: 0; left: 0; right: 0;
    height: 10px; background: var(--navy);
    border-bottom: 3px solid var(--rust);
  }
  .band-bottom {
    position: absolute; bottom: 0; left: 0; right: 0;
    height: 28px; background: var(--navy);
    border-top: 3px solid var(--rust);
  }
  .card-front .wordmark {
    position: absolute;
    left: 26px; bottom: 72px;
    color: var(--navy);
    font-weight: 800;
    font-size: 110px;
    line-height: 1;
    letter-spacing: 2px;
  }
  .identity {
    position: absolute;
    left: 400px; top: 70px;
    width: 280px;
    border-bottom: 1.5px solid var(--navy);
    padding-bottom: 6px;
  }
  .identity .name {
    color: var(--navy);
    font-size: 22px;
    line-height: 1.1;
  }
  .identity .name .first { font-weight: 800; }
  .identity .name .last { font-weight: 600; font-size: 17px; }
  .identity .title {
    color: var(--ink-grey);
    font-size: 11.5px;
    margin-top: 2px;
  }
  .contacts {
    position: absolute;
    left: 400px; top: 160px;
    list-style: none;
  }
  .contacts li {
    display: flex;
    align-items: center;
    gap: 10px;
    color: var(--ink-grey);
    font-size: 15px;
    height: 28px;
  }
  .contacts li.address {
    font-size: 12px;
    line-height: 1.25;
    text-transform: uppercase;
    height: auto;
    align-items: flex-start;
    padding-top: 2px;
  }
  .icon-box {
    width: 22px; height: 22px;
    background: var(--navy);
    border-radius: 2px;
    flex: 0 0 22px;
    display: flex; align-items: center; justify-content: center;
  }
  .icon-box svg { width: 14px; height: 14px; }
</style>
</head>
<body>

  <section class="card card-back" aria-label="Back of business card">
    <div class="wordmark">DK&amp;R</div>
    <div class="web-rule">
      <span class="rule"></span>
      <span class="web">www.dkrfabworks.example</span>
      <span class="rule right"></span>
    </div>
  </section>

  <section class="card card-front" aria-label="Front of business card">
    <div class="band-top"></div>

    <div class="wordmark">DK&amp;R</div>

    <div class="identity">
      <p class="name"><span class="first">Glenn</span> <span class="last">Harwick</span></p>
      <p class="title">Business Development Manager</p>
    </div>

    <ul class="contacts">
      <li>
        <span class="icon-box">
          <svg viewBox="0 0 16 16" fill="none" stroke="#fff" stroke-width="1.3"><circle cx="8" cy="8" r="6.5"/><path d="M5.5 4.5l1.3 1.6-.8 1a4.5 4.5 0 0 0 2.9 2.9l1-.8 1.6 1.3-.7 1.1c-3.3-.4-5.9-3-6.3-6.3z" fill="#fff" stroke="none"/></svg>
        </span>
        205-555-0148
      </li>
      <li>
        <span class="icon-box">
          <svg viewBox="0 0 16 16" fill="none" stroke="#fff" stroke-width="1.3"><rect x="2" y="4" width="12" height="8.5"/><path d="M2 4l6 5 6-5"/></svg>
        </span>
        harwickg@dkrfabworks.example
      </li>
      <li>
        <span class="icon-box">
          <svg viewBox="0 0 16 16" fill="none" stroke="#fff" stroke-width="1.1"><circle cx="8" cy="8" r="6"/><ellipse cx="8" cy="8" rx="2.6" ry="6"/><path d="M2 8h12M3 5h10M3 11h10"/></svg>
        </span>
        www.dkrfabworks.example
      </li>
      <li class="address">
        <span class="icon-box">
          <svg viewBox="0 0 16 16"><path d="M8 1.5a4.3 4.3 0 0 0-4.3 4.3C3.7 9 8 14.5 8 14.5s4.3-5.5 4.3-8.7A4.3 4.3 0 0 0 8 1.5z" fill="#fff"/><circle cx="8" cy="5.8" r="1.6" fill="#1d3566"/></svg>
        </span>
        <span>418 Wendlow Ridge Drive,<br>Suite 340 Birmingham, AL 35242</span>
      </li>
    </ul>

    <div class="band-bottom"></div>
  </section>

</body>
</html>
```